Insulation Franchise Seasonal Content Creation

I am looking to launch some seasonal content and I would like 8 different designs that will go out as digital ads, Facebook and Instagram posts. The look and feel of the design: - Clean and neat - Simple Text, lots of open space (don’t want it to look too crowded) - Using branded colors that give a winter feel (brand guide to be provided) - Two separate texts areas in the design 1.) A sentence that identifies the pain point and explains the picture 2.) A sentence that is the call to action. See the attached ads for a general idea of the look we would like but I would like this design to stand out from those. I will provide copy, photos, branded colors, fonts and logos. Here is the copy I would like to use:
“Feeling the winter this year?” (pic of cold coming inside) “Let Wombi help keep the cold outside”
“Feel the winter creeping in?” “Air sealing and proper Insulation can eliminate those cool winter breezes in your home.”

“High heating bills? Why are you paying to melt the snow and ice on your roof?”
“Get your home well insulated with Wombi and keep your heat INSIDE where it should be” (Patchy snow on roofs)
“Storm damage to your home?” “Wombi can help by replacing wet and ruined insulation” (Before and after pics of damage)

Holiday Pain Points - Saving money / Visitors comfortability
“Snow on the roof means a well insulated home. Leave the snow for Santa to land on this year.” “Click here to learn how to keep your home comfortable and lower heating bills this winter” (pic of santa’s boots on the roof)
“Family complaining about the temperature in your house? Make sure your guests stay comfortable this holiday season” (pic of someone cold inside)
“Staying home this holiday season? Be comfortable and ensure your home is well-insulated.” “Contact Wombi for a free estimate”
Keep your money to spend on your holidays, not on your heating bill! Let Wombi help you save by correctly insulating your home!”

Target Market(s)

Homeowners, those interested in savings in their heating/cooling costs, energy efficiency

Industry/Entity Type

Home Improvement

Font styles to use
Sans Serif
Other font styles liked:
• Honey Lips, Bolt Rounded

Colors
0054AA
0677BA
7BADD7
CADEEF
E8F1F8
0094D4
00A9DD
6FCCEA
C7EBF8
E9F6FB
00AB8E
00BBA5
67D7C9
C6EFE9
E9F9F6

Requirements
Must have
• 2 separate text areas, photo and the logo
Should not have
• No pictures of the mascot, Tavo (the Wombi bear)

```html
<!DOCTYPE html>
<html lang="en">
<head>
<meta charset="utf-8">
<title>Wombi Insulation – High Heating Bills Ad</title>
<link rel="stylesheet" href="https://fonts.googleapis.com/css2?family=Poppins:wght@300;400;700&display=swap">
<style>
  :root {
    --backdrop: #b1b1b1;
    --photo-warm: #c9433b;
    --photo-light: #ece7e3;
    --photo-dark: #3a2a26;
    --brand-green: #5fbf2a;
    --brand-green-soft: rgba(88, 184, 34, 0.82);
    --brand-blue: rgba(0, 84, 170, 0.62);
    --text-light: #ffffff;
  }
  * { margin: 0; padding: 0; box-sizing: border-box; }
  html, body {
    width: 1200px;
    height: 1025px;
    overflow: hidden;
    background: var(--backdrop);
    font-family: "Poppins", sans-serif;
  }
  .ad {
    position: absolute;
    left: 322px;
    top: 234px;
    width: 555px;
    height: 555px;
    overflow: hidden;
  }
  .ad__photo {
    position: absolute;
    inset: 0;
    background:
      radial-gradient(ellipse 38% 48% at 45% 45%, var(--photo-warm) 0%, rgba(201,67,59,0.85) 55%, rgba(201,67,59,0) 100%),
      linear-gradient(90deg, #3f5a2c 0%, #5a3b30 12%, var(--photo-dark) 30%, #8f8580 55%, var(--photo-light) 72%, #f3efec 100%);
  }
  .ad__shapes {
    position: absolute;
    inset: 0;
  }
  .ad__logo {
    position: absolute;
    right: 30px;
    top: 48px;
    display: flex;
    align-items: center;
    gap: 8px;
    color: var(--brand-green);
    font-weight: 700;
    font-size: 22px;
    letter-spacing: 0.3px;
  }
  .ad__logo-dot {
    width: 12px;
    height: 12px;
    border-radius: 50%;
    background: var(--brand-green);
  }
  .ad__tagline {
    position: absolute;
    left: 38px;
    bottom: 17px;
    transform-origin: left bottom;
    transform: rotate(-90deg) translateY(100%);
    color: var(--text-light);
    font-weight: 300;
    font-size: 11px;
    letter-spacing: 0.4px;
    white-space: nowrap;
  }
  .ad__message {
    position: absolute;
    right: 23px;
    top: 395px;
    text-align: right;
    color: var(--text-light);
  }
  .ad__headline {
    font-weight: 700;
    font-size: 31px;
    line-height: 38px;
    letter-spacing: -0.5px;
  }
  .ad__subline {
    font-weight: 400;
    font-size: 23px;
    line-height: 25px;
    letter-spacing: -0.3px;
  }
</style>
</head>
<body>
  <section class="ad">
    <div class="ad__photo" role="img" aria-label="Stressed man in a red sweater holding his head while reading a heating bill at a desk beside a decorated Christmas tree"></div>

    <svg class="ad__shapes" viewBox="0 0 555 555" width="555" height="555" aria-hidden="true">
      <polygon points="147,398 294,330 555,354 555,555 206,555" fill="var(--brand-green-soft)"/>
      <polygon points="0,462 150,555 0,555" fill="var(--brand-blue)"/>
    </svg>

    <div class="ad__logo">
      <span class="ad__logo-dot"></span>
      <span class="ad__logo-name">Wombi Insulation</span>
    </div>

    <p class="ad__tagline">We Make Home Comfortable.</p>

    <div class="ad__message">
      <h1 class="ad__headline">HIGH HEATING BILLS?</h1>
      <p class="ad__subline">Why are you paying<br>to melt the snow<br>and ice on your roof?</p>
    </div>
  </section>
</body>
</html>
```